Aviation security consulting company needs a website

We need a website design for Brisk Holloway, and aviation security consulting company. Brisk Holloway (www.briskholloway.example) is an aviation security consulting company that works with government and industry stakeholders in over 60 countries on aviation security strategy, governance, and oversight at the regulatory and operational level.
Brisk Holloway is strongly internationally focused.
The website required should be simple, corporate, serious, and communicate professionalism, reliability and honesty. We are trying to give the company a feeling of being well established.
The attached files include the company logo, along with examples of company web page styles that we like.
The Brisk Holloway website need only be around five pages long (landing page, who we are, our services, our clients, contact), though don't feel limited to only five pages.
The existing website (www.briskholloway.example) was rushed and put together using Wix. We don't love the existing website as it looks too amateur, so don't use it as a template.
There is no requirement for any online sales tools to be included in the site. The site is purely informational, with the option of people making contact via email.

```html
<!DOCTYPE html>
<html lang="en">
<head>
<meta charset="utf-8">
<title>Brisk Holloway – Aviation Security Consulting</title>
<link href="https://fonts.googleapis.com/css2?family=Carlito:wght@400;700&display=swap" rel="stylesheet">
<style>
:root{
  --page-bg:#2a1c10;
  --header-bg:#ffffff;
  --brand-navy:#1f3060;
  --brand-grey:#4a4a4a;
  --menu-bg:#000000;
  --menu-text:#ffffff;
  --menu-active:#6f8fe6;
  --panel-blue:rgba(50,72,140,0.78);
  --card-band:rgba(52,74,140,0.72);
  --text-light:#ffffff;
}
*{margin:0;padding:0;box-sizing:border-box}
html,body{width:1200px;height:902px;overflow:hidden}
body{
  position:relative;
  font-family:"Carlito",sans-serif;
  color:var(--text-light);
  background:radial-gradient(ellipse at 50% 40%,#5a3a1a 0%,#3a2612 45%,#1c130a 100%);
}
.site-header{
  position:absolute;left:120px;top:25px;width:960px;height:77px;
  background:var(--header-bg);z-index:5;
}
.brand{position:absolute;left:15px;top:8px;display:flex;align-items:center;gap:10px}
.brand-square{width:60px;height:60px;background:var(--brand-navy)}
.brand-text{display:flex;flex-direction:column}
.brand-name{font-size:33px;font-weight:700;color:var(--brand-navy);line-height:1}
.brand-tagline{font-size:14px;letter-spacing:2.6px;color:var(--brand-grey);margin-top:2px}
.menu-toggle{position:absolute;left:926px;top:27px}
.dropdown{
  position:absolute;left:927px;top:72px;width:138px;height:168px;
  background:var(--menu-bg);list-style:none;padding-top:13px;z-index:20;
}
.dropdown li{height:32px;padding-left:33px;font-size:10.5px;position:relative;line-height:14px}
.dropdown li::before{content:"";position:absolute;left:33px;top:4px;width:4px;height:6px;background:var(--menu-text)}
.dropdown li a{color:var(--menu-text);text-decoration:none;padding-left:11px}
.dropdown li.active::before{background:var(--menu-active)}
.dropdown li.active a{color:var(--menu-active);font-weight:700}
.hero{
  position:absolute;left:120px;top:125px;width:960px;height:429px;z-index:1;
  background:linear-gradient(180deg,#6e6a66 0%,#8e7d68 35%,#c9874a 62%,#7a4a28 80%,#3e2a1c 100%);
}
.hero-panel{
  position:absolute;left:234px;top:151px;width:492px;height:164px;
  background:var(--panel-blue);text-align:center;
}
.hero-title{font-size:26px;font-weight:700;margin-top:12px;line-height:30px}
.hero-copy{font-size:10.5px;line-height:19px;margin-top:5px;padding:0 40px}
.btn-outline{
  display:inline-block;margin-top:7px;width:99px;height:25px;line-height:23px;
  border:1px solid #fff;font-size:10.5px;color:#fff;text-decoration:none;
}
.slider-dots{position:absolute;left:455px;top:387px;display:flex;gap:12px}
.slider-dots span{width:9px;height:11px;background:rgba(255,255,255,.5)}
.slider-dots span.on{background:#fff}
.cards{position:absolute;top:579px;left:120px;width:960px;display:flex;gap:19px}
.card{position:relative;width:307px;height:207px}
.card-who{background:linear-gradient(135deg,#e8eef2,#a9b3bd 60%,#5b5f66)}
.card-services{background:linear-gradient(135deg,#c9d3dc,#6e7884 55%,#2c2e34)}
.card-clients{background:linear-gradient(135deg,#8a9aa8,#3c4656 55%,#1a1c22)}
.card-band{
  position:absolute;left:0;top:47px;width:100%;height:107px;
  background:var(--card-band);text-align:center;
}
.card-title{font-size:16px;font-weight:400;margin-top:13px;line-height:18px}
.card-copy{font-size:10.5px;line-height:19px;margin-top:4px;padding:0 30px}
.card-link{display:inline-flex;align-items:center;gap:5px;font-size:11px;color:#fff;text-decoration:none;margin-top:5px}
.site-footer{position:absolute;left:0;top:823px;width:1200px;text-align:center;font-size:10.5px}
.footer-nav a{color:#fff;text-decoration:none}
.footer-nav .sep{margin:0 7px}
.copyright{margin-top:15px}
</style>
</head>
<body>
<header class="site-header">
  <div class="brand">
    <div class="brand-square"></div>
    <div class="brand-text">
      <span class="brand-name">Brisk Holloway</span>
      <span class="brand-tagline">aviation security consulting</span>
    </div>
  </div>
  <svg class="menu-toggle" width="18" height="18" viewBox="0 0 18 18" aria-label="Menu">
    <g fill="#111">
      <rect x="0" y="0" width="4" height="4"/><rect x="7" y="0" width="4" height="4"/><rect x="14" y="0" width="4" height="4"/>
      <rect x="0" y="7" width="4" height="4"/><rect x="7" y="7" width="4" height="4"/><rect x="14" y="7" width="4" height="4"/>
      <rect x="0" y="14" width="4" height="4"/><rect x="7" y="14" width="4" height="4"/><rect x="14" y="14" width="4" height="4"/>
    </g>
  </svg>
</header>
<ul class="dropdown">
  <li class="active"><a href="#">Home</a></li>
  <li><a href="#">Who We Are</a></li>
  <li><a href="#">Our Services</a></li>
  <li><a href="#">Our Clients</a></li>
  <li><a href="#">Contact</a></li>
</ul>

<section class="hero" role="img" aria-label="Airport terminal at sunset with an airliner, world map and business travellers shaking hands">
  <div class="hero-panel">
    <h1 class="hero-title">Security Consulting Company</h1>
    <p class="hero-copy">If you are going to use a passage of Lorem Ipsum, you need to be sure there isn't anything embarrassing hidden in the middle of text. All the Lorem Ipsum generators on the Internet making this the first true generator on the Internet.</p>
    <a class="btn-outline" href="#">More Info</a>
  </div>
  <div class="slider-dots"><span class="on"></span><span></span><span></span></div>
</section>

<section class="cards">
  <article class="card card-who" role="img" aria-label="Business people meeting with a laptop in a bright office">
    <div class="card-band">
      <h2 class="card-title">Who We Are</h2>
      <p class="card-copy">If you are going to use a passage of Lorem Ipsum, you need to be sudden in the middle of text.</p>
      <a class="card-link" href="#">More Info <svg width="8" height="8" viewBox="0 0 8 8"><circle cx="4" cy="4" r="4" fill="#fff"/><path d="M3 2l2 2-2 2" stroke="#34488c" stroke-width="1.3" fill="none"/></svg></a>
    </div>
  </article>
  <article class="card card-services" role="img" aria-label="Businesswoman with a tablet at an airport">
    <div class="card-band">
      <h2 class="card-title">Services</h2>
      <p class="card-copy">If you are going to use a passage of Lorem Ipsum, you need to be sudden in the middle of text.</p>
      <a class="card-link" href="#">More Info <svg width="8" height="8" viewBox="0 0 8 8"><circle cx="4" cy="4" r="4" fill="#fff"/><path d="M3 2l2 2-2 2" stroke="#34488c" stroke-width="1.3" fill="none"/></svg></a>
    </div>
  </article>
  <article class="card card-clients" role="img" aria-label="Traveller working on a laptop in an airport terminal">
    <div class="card-band">
      <h2 class="card-title">Our Clients</h2>
      <p class="card-copy">If you are going to use a passage of Lorem Ipsum, you need to be sudden in the middle of text.</p>
      <a class="card-link" href="#">More Info <svg width="8" height="8" viewBox="0 0 8 8"><circle cx="4" cy="4" r="4" fill="#fff"/><path d="M3 2l2 2-2 2" stroke="#34488c" stroke-width="1.3" fill="none"/></svg></a>
    </div>
  </article>
</section>

<footer class="site-footer">
  <nav class="footer-nav">
    <a href="#">Home</a><span class="sep">|</span><a href="#">Who We Are</a><span class="sep">|</span><a href="#">Our Services</a><span class="sep">|</span><a href="#">Our Clients</a><span class="sep">|</span><a href="#">Contact</a>
  </nav>
  <p class="copyright">© 2016 Brisk Holloway. All rights reserved.</p>
</footer>
</body>
</html>
```